Harbour Pizza gazebo signage project.

We are looking for signage for our mobile pizzeria gazebo structure. We sell pizza from a woodfired oven, Neapolitan style. We have a KR campervan which we sell pizza from too, which is yellow and black, so we would like to stick with those colours. The signage needs to be 2, 305cm x 76cm one for the top, and one for the bottom. It needs to state clearly the product is pizza. It also needs to include our logo, our website and that we sell Neapolitan style woodfired pizza. Our website is harbourpizza.co.uk to get a feel of our brand. We also don't want photos of pizza on the design.

Colors
000000
fbed22

Requirements
Must have
• The colours yellow and black and our logo on the top banner. Our website and the pinlane, tallyo and snapmoor logos on the bottom banner.

```html
<!DOCTYPE html>
<html lang="en">
<head>
<meta charset="utf-8">
<title>Harbour Pizza gazebo banners</title>
<link rel="stylesheet" href="https://fonts.googleapis.com/css2?family=Montserrat:wght@500;800&display=swap">
<style>
  :root {
    --brand-yellow: #fbed22;
    --brand-black: #000000;
    --accent-shade: rgba(0, 0, 0, 0.22);
    --divider: #ffffff;
  }
  html, body {
    margin: 0;
    padding: 0;
    width: 1200px;
    height: 603px;
    overflow: hidden;
    background: var(--divider);
  }
  .signage {
    position: relative;
    width: 1200px;
    height: 603px;
    font-family: "Montserrat", Arial, sans-serif;
    color: var(--brand-black);
  }
  .banner {
    position: absolute;
    left: 0;
    width: 1200px;
    background: var(--brand-yellow);
    overflow: hidden;
  }
  .banner--top { top: 0; height: 300px; }
  .banner--bottom { top: 302px; height: 301px; }

  .ornament-area {
    position: absolute;
    background: radial-gradient(ellipse at center, var(--accent-shade) 0%, rgba(0, 0, 0, 0) 70%);
  }
  .banner--top .ornament-area--upper { left: 545px; top: -20px; width: 620px; height: 80px; }
  .banner--top .ornament-area--lower { left: 470px; top: 250px; width: 500px; height: 70px; }
  .banner--bottom .ornament-area--upper { left: 0; top: -15px; width: 860px; height: 80px; }
  .banner--bottom .ornament-area--lower { left: 560px; top: 225px; width: 620px; height: 90px; }

  .brand-mark {
    position: absolute;
    left: 20px;
    top: 16px;
    width: 270px;
    height: 270px;
    box-sizing: border-box;
    border: 6px solid var(--brand-black);
    border-radius: 50%;
    display: flex;
    flex-direction: column;
    align-items: center;
    justify-content: center;
    font-weight: 800;
    font-size: 40px;
    line-height: 1.1;
    text-transform: uppercase;
    text-align: center;
  }
  .website {
    position: absolute;
    margin: 0;
    font-weight: 800;
    white-space: nowrap;
    letter-spacing: -1px;
    line-height: 1;
  }
  .tagline {
    position: absolute;
    margin: 0;
    font-weight: 500;
    white-space: nowrap;
    line-height: 1;
  }
  .banner--top .website { left: 316px; top: 84px; font-size: 66px; }
  .banner--top .tagline { left: 318px; top: 176px; font-size: 41px; }
  .banner--bottom .website { left: 20px; top: 100px; font-size: 56px; }
  .banner--bottom .tagline { left: 22px; top: 174px; font-size: 35px; }

  .social-list {
    position: absolute;
    left: 820px;
    width: 360px;
    top: 133px;
    margin: 0;
    padding: 0;
    list-style: none;
    display: flex;
    justify-content: space-between;
    font-weight: 800;
    font-size: 27px;
    line-height: 1;
  }
</style>
</head>
<body>
<main class="signage">
  <section class="banner banner--top" aria-label="Top banner">
    <div class="ornament-area ornament-area--upper" role="img" aria-label="Decorative black swoosh lines"></div>
    <div class="ornament-area ornament-area--lower" role="img" aria-label="Decorative black swoosh line"></div>
    <div class="brand-mark"><span>Harbour</span><span>Pizza</span></div>
    <h1 class="website">www.harbourpizza.co.uk</h1>
    <p class="tagline">We sell Neapolitan style woodfired pizza</p>
  </section>
  <section class="banner banner--bottom" aria-label="Bottom banner">
    <div class="ornament-area ornament-area--upper" role="img" aria-label="Decorative black swoosh lines"></div>
    <div class="ornament-area ornament-area--lower" role="img" aria-label="Decorative black swoosh lines"></div>
    <h2 class="website">www.harbourpizza.co.uk</h2>
    <p class="tagline">We sell Neapolitan style woodfired pizza</p>
    <ul class="social-list" aria-label="Social channels">
      <li>tallyo</li>
      <li>snapmoor</li>
      <li>pinlane</li>
    </ul>
  </section>
</main>
</body>
</html>
```